Defense Attorney Business Card Design Project/ Stationary

I am looking for a distinctive business card design for my solo law practice.
I practice criminal defense, both juvenile and adult, including DUI. I am a very experienced attorney with prior military experience. The design should convey a traditional, old school flair, but not be too stodgy or uptight. Some color. My logo should appear.

Project Deadline Extended Reason: I misunderstood how this project works and I was not prepared with my logo when this project ran the first time. Added Thursday, November 13, 2014

Reason: I was sent overseas on military duty last year, which interrupted this project. Thank you for your participation... I hope we can get this done this week! Thank you, Des

Target Market(s)

Regular everyday people looking for strong, knowledgeable, authoritative representation while they are faced with criminal charges. Many have never been charged with a crime before. A reassuring air is therefore desired.

Industry/Entity Type

Business

Contact Information for Business Card

My information is:
Desmond R. Whitcombe, Attorney at Law
735 Linden Avenue Suite 300
Oakland, California 94618
Tel: (510) 555-0183
Fax: (510) 555-0162
email: deswhitcombelaw@mailbrook.net
web: www.deswhitcombelaw.net

Font styles to use
Serif
Sans Serif
Decorative

Colors
0255a3
ffffff

Requirements
Must have
• Sharp lines, bold elements. Conservative use of colors, such as deep blues, burgundy, grays for example.
• While my logo says "Des Whitcombe", it should be modified to show "Desmond R. Whitcombe".
Should not have
• Cliche imagery such as scales of justice, gavels, Tower of Varenholt, etc.

```html
<!DOCTYPE html>
<html lang="en">
<head>
<meta charset="utf-8">
<title>Criminal Defense Attorney – Business Card</title>
<link rel="stylesheet" href="https://fonts.googleapis.com/css2?family=Oswald:wght@700&family=Poiret+One&display=swap">
<style>
  :root {
    --kraft: #d8b389;
    --kraft-light: #ddbb93;
    --kraft-dark: #d1ab80;
    --stripe-red: #b8292b;
    --ink: #111111;
    --ink-soft: #2b2622;
  }
  html, body {
    margin: 0;
    padding: 0;
    width: 1200px;
    height: 805px;
    overflow: hidden;
  }
  .card {
    position: relative;
    width: 1200px;
    height: 805px;
    overflow: hidden;
    background: radial-gradient(ellipse at 60% 45%, var(--kraft-light) 0%, var(--kraft) 55%, var(--kraft-dark) 100%);
  }
  .stripes {
    position: absolute;
    inset: 0;
    width: 1200px;
    height: 805px;
  }
  .stripes line {
    stroke: var(--stripe-red);
    stroke-width: 11;
  }
  .title {
    position: absolute;
    left: 144px;
    top: 262px;
    margin: 0;
    font-family: "Oswald", "Arial Narrow", sans-serif;
    font-weight: 700;
    font-size: 86px;
    line-height: 1;
    letter-spacing: 1px;
    color: var(--ink);
    white-space: nowrap;
  }
  .role {
    position: absolute;
    left: 586px;
    top: 342px;
    margin: 0;
    font-family: "Poiret One", sans-serif;
    font-weight: 400;
    font-size: 76px;
    line-height: 1;
    color: var(--ink-soft);
    white-space: nowrap;
  }
  .details {
    position: absolute;
    left: 586px;
    top: 602px;
    margin: 0;
    font-family: "Poiret One", sans-serif;
    color: var(--ink-soft);
    white-space: nowrap;
  }
  .details .lead {
    display: block;
    font-size: 45px;
    line-height: 52px;
  }
  .details .line {
    display: block;
    font-size: 30px;
    line-height: 30px;
  }
</style>
</head>
<body>
  <div class="card">
    <svg class="stripes" viewBox="0 0 1200 805" aria-hidden="true">
      <line x1="454" y1="-10" x2="-150" y2="795"/>
      <line x1="500" y1="-10" x2="-104" y2="795"/>
      <line x1="548" y1="-10" x2="-56" y2="795"/>
      <line x1="592" y1="-10" x2="-12" y2="795"/>
      <line x1="638" y1="-10" x2="34" y2="795"/>
      <line x1="684" y1="-10" x2="80" y2="795"/>
    </svg>

    <h1 class="title">CRIMINAL DEFENSE</h1>
    <p class="role">Attorney</p>

    <p class="details">
      <span class="lead">Some information</span>
      <span class="line">Some information</span>
      <span class="line">Some information</span>
    </p>
  </div>
</body>
</html>
```